Meridane Works, Inc. - Update our Website

Meridane Works needs a website to help our customers to navigate through our services efficiently. Our existing website is at www.meridwork.example

We would like to explain our services with content and pictures (photographs) that distinguishes our products and services from our competition.

The website design must implement a strategy to focus on our Contract Labeling services.

With this new design we would like to attract new customers and ensure that our existing customers are fully informed with our latest offerings.

```html
<!DOCTYPE html>
<html lang="en">
<head>
<meta charset="utf-8">
<title>Meridane Works, Inc.</title>
<link rel="stylesheet" href="https://fonts.googleapis.com/css2?family=PT+Sans:ital,wght@0,400;0,700;1,700&family=Ubuntu:wght@300;400&display=swap">
<style>
:root{
  --outer:#ececec;
  --page:#ffffff;
  --ink:#222222;
  --body:#6a6a6a;
  --nav:#666666;
  --blue:#2f6bff;
  --blue-btn:#2a7cf0;
  --teal:#45c39f;
  --panel:#efefef;
  --footer:#2b2b2b;
  --footer-base:#222222;
  --footer-text:#bdbdbd;
  --footer-line:#3f3f3f;
}
*{margin:0;padding:0;box-sizing:border-box}
html,body{width:1200px;height:2289px;overflow:hidden;background:var(--outer)}
body{position:relative;font-family:"Ubuntu",sans-serif;color:var(--body)}
.page{position:absolute;left:36px;top:0;width:1116px;height:2289px;background:var(--page)}
.site-header{position:absolute;left:0;top:0;width:1200px;height:105px;background:var(--page)}
.brand{position:absolute;left:84px;top:26px;display:flex;align-items:center;gap:14px}
.brand-dot{width:52px;height:52px;border-radius:50%;background:var(--teal)}
.brand-name{font-family:"PT Sans",sans-serif;font-weight:700;font-size:30px;color:#4a4a4a;letter-spacing:1px}
.main-nav{position:absolute;right:78px;top:39px;display:flex;gap:28px;align-items:center;font-family:"PT Sans",sans-serif;font-size:15px;color:var(--nav)}
.main-nav .active{color:var(--ink)}
.hero{position:absolute;left:36px;top:105px;width:1116px;height:536px;background:linear-gradient(110deg,#cfe0ee 0%,#9fc3e0 30%,#c9d4dc 55%,#8e9ba4 100%)}
.hero-banner{position:absolute;left:34px;top:360px;width:1050px;height:111px;background:var(--blue);opacity:.93;padding:16px 24px}
.hero-banner h1{font-family:"PT Sans",sans-serif;font-style:italic;font-weight:700;font-size:37px;line-height:44px;color:#fff;text-transform:uppercase}
.intro{position:absolute;left:70px;top:706px;width:1050px;height:147px;background:var(--panel);border-left:5px solid var(--teal);border-radius:3px}
.intro p{position:absolute;left:30px;top:34px;width:790px;font-family:"PT Sans",sans-serif;font-weight:700;font-size:17px;line-height:26px;color:var(--ink);text-transform:uppercase}
.intro .btn{position:absolute;left:921px;top:38px;width:92px;height:42px;background:var(--blue-btn);color:#fff;border-radius:3px;font-family:"PT Sans",sans-serif;font-weight:700;font-size:14px;display:flex;align-items:center;justify-content:center}
.section-title{position:absolute;left:70px;font-family:"PT Sans",sans-serif;font-weight:700;font-size:23px;color:var(--ink)}
.card{position:absolute;width:232px;text-align:center}
.thumb{display:block;width:60px;height:60px;border-radius:50%;margin:0 auto;border:2px solid #d8e8e4}
.plus{display:block;margin:0 auto}
.card h3{font-family:"PT Sans",sans-serif;font-weight:700;font-size:18px;line-height:24px;color:var(--ink);margin-top:14px;text-transform:uppercase}
.card p{font-size:13.4px;line-height:25px;color:var(--body);margin-top:6px}
.card .more-link{display:block;font-size:13.4px;color:var(--teal);margin-top:10px}
.site-footer{position:absolute;left:36px;top:1980px;width:1116px;height:281px;background:var(--footer)}
.footer-base{position:absolute;left:36px;top:2261px;width:1116px;height:28px;background:var(--footer-base)}
.footer-col{position:absolute;top:52px;width:326px}
.footer-col h4{font-family:"PT Sans",sans-serif;font-weight:700;font-size:18px;color:#fff;text-transform:uppercase;margin-bottom:12px}
.footer-col li{list-style:none;font-size:13px;color:var(--footer-text);padding:8px 10px;border-bottom:1px solid var(--footer-line);height:33px}
</style>
</head>
<body>
<div class="page"></div>

<header class="site-header">
  <div class="brand"><span class="brand-dot"></span><span class="brand-name">MERIDANE WORKS, INC.</span></div>
  <nav class="main-nav">
    <span>ABOUT US</span><span class="active">PRODUCTS</span><span>USER SUPPORT</span><span>CONTACT US</span>
    <svg width="16" height="16" viewBox="0 0 16 16"><circle cx="6.5" cy="6.5" r="4.5" fill="none" stroke="#777" stroke-width="1.6"/><line x1="10" y1="10" x2="14" y2="14" stroke="#777" stroke-width="1.8"/></svg>
  </nav>
</header>

<section class="hero" role="img" aria-label="Photograph of a technician in cleanroom gear operating pharmaceutical production equipment">
  <div class="hero-banner"><h1>Products and services for the pharmaceutical<br>industry</h1></div>
</section>

<section class="intro">
  <p>Meridane Works, Inc. specializes in providing products and services to the pharmaceutical industry. We are focused on the needs of those individuals involved with clinical trial materials.</p>
  <span class="btn">MORE</span>
</section>

<h2 class="section-title" style="top:908px">SERVICES</h2>

<article class="card" style="left:72px;top:1006px">
  <span class="thumb" role="img" aria-label="Service photo thumbnail" style="background:radial-gradient(circle,#8a8f99,#4b5563)"></span>
  <h3>MeriServ™</h3>
  <p>MeriServ™ is a contract clinical label generation service that provides you with ready to apply clinical labels specifically designed and produced for your clinical trial needs. The service enables you to obtain blinded and open study labeling with a broad range of variable data elements. Our exclusive MeriPro/LBL™ computer systems…</p>
  <span class="more-link">Read more</span>
</article>
<article class="card" style="left:343px;top:1006px">
  <span class="thumb" role="img" aria-label="Service photo thumbnail" style="background:radial-gradient(circle,#5b8ee0,#0d1f4f)"></span>
  <h3>MeriBook™</h3>
  <p>MeriBook™ labels include multiple pages of study information within each clinical label to address the needs of multi-language studies. This enables users to prepare and ship clinical materials to multiple countries without having to utilize country specific labels. These labels are applied to clinical materials in the same manner as…</p>
  <span class="more-link">Read more</span>
</article>
<article class="card" style="left:614px;top:1006px">
  <span class="thumb" role="img" aria-label="Service photo thumbnail" style="background:radial-gradient(circle,#e8f0ec,#7fb7a4)"></span>
  <h3>Clinical Randomization</h3>
  <p>Our systems can create randomization data for all types of CTM requirements. Patient randomization, material randomization and random sequence coding can be produced to suit your data needs for any type of clinical trial. Data is generated using our validated MeriPro/LBL™ system in a qualified environment. Our capabilities include: Patient…</p>
  <span class="more-link">Read more</span>
</article>
<article class="card" style="left:885px;top:1006px">
  <svg class="plus" width="60" height="60" viewBox="0 0 60 60"><circle cx="30" cy="30" r="28" fill="#fff" stroke="var(--teal)" stroke-width="2"/><line x1="30" y1="16" x2="30" y2="44" stroke="#333" stroke-width="2.5"/><line x1="16" y1="30" x2="44" y2="30" stroke="#333" stroke-width="2.5"/></svg>
  <h3>More</h3>
  <p>Lorem ipsum dolor sit amet, consectetur adipiscing elit, sed do eiusmod tempor incididunt ut labore et dolore magna aliqua. Ut enim ad minim veniam, quis nostrud exercitation ullamco laboris nisi ut aliquip ex ea commodo consequat. Duis aute irure dolor in reprehenderit in voluptate velit esse cillum dolore eu fugiat…</p>
  <span class="more-link">Read more</span>
</article>

<h2 class="section-title" style="top:1414px">SOFTWARE PRODUCTS</h2>

<article class="card" style="left:72px;top:1513px">
  <span class="thumb" role="img" aria-label="Product photo thumbnail" style="background:radial-gradient(circle,#c58be0,#5a1f7a)"></span>
  <h3>MeriPro/LBL™</h3>
  <p>MeriPro/LBL™ is the industry's leading clinical label generation system offering superior overall capability and flexibility. The system enables users to generate all of their clinical labeling requirements from a rich computer model of a clinical protocol in a Panelia™ environment. Sophisticated patient and materials randomizations can be generated or imported…</p>
  <span class="more-link">Read more</span>
</article>
<article class="card" style="left:343px;top:1513px">
  <span class="thumb" role="img" aria-label="Product photo thumbnail" style="background:radial-gradient(circle,#6fd0c8,#1c2d5a)"></span>
  <h3>Software Validation<br>Service</h3>
  <p>Meridane Works offers Software Validation Services for the FDA regulated pharmaceutical industry. Our knowledge of industry practices and standards along with regulatory requirements, enable us to create practical and cost-effective solutions for your validation needs. We have been performing computer systems validation for over 20 years. This experience with the…</p>
  <span class="more-link">Read more</span>
</article>
<article class="card" style="left:614px;top:1513px">
  <span class="thumb" role="img" aria-label="Product photo thumbnail" style="background:radial-gradient(circle,#f0c060,#7a4a10)"></span>
  <h3>MeriStock™</h3>
  <p>MeriStock™ is a premium line of label stock products that Meridane Works supplies to the pharmaceutical industry. These label stocks are specifically designed for use by clinical supply departments for the computer printing of clinical study labels. Labels are available from our in-house inventories or converted for you on a…</p>
  <span class="more-link">Read more</span>
</article>
<article class="card" style="left:885px;top:1513px">
  <svg class="plus" width="60" height="60" viewBox="0 0 60 60"><circle cx="30" cy="30" r="28" fill="#fff" stroke="var(--teal)" stroke-width="2"/><line x1="30" y1="16" x2="30" y2="44" stroke="#333" stroke-width="2.5"/><line x1="16" y1="30" x2="44" y2="30" stroke="#333" stroke-width="2.5"/></svg>
  <h3>More</h3>
  <p>Lorem ipsum dolor sit amet, consectetur adipiscing elit, sed do eiusmod tempor incididunt ut labore et dolore magna aliqua. Ut enim ad minim veniam, quis nostrud exercitation ullamco laboris nisi ut aliquip ex ea commodo consequat. Duis aute irure dolor in reprehenderit in voluptate velit esse cillum dolore eu fugiat…</p>
  <span class="more-link">Read more</span>
</article>

<footer class="site-footer">
  <div class="footer-col" style="left:33px">
    <h4>Menu</h4>
    <ul><li>About Us</li><li>Contact Us</li><li>Products</li><li>User Support</li></ul>
  </div>
  <div class="footer-col" style="left:395px">
    <h4>Services</h4>
    <ul><li>MERIBOOK™</li><li>Clinical Randomization</li><li>MeriServ™</li></ul>
  </div>
  <div class="footer-col" style="left:756px">
    <h4>Software Products</h4>
    <ul><li>Clinical Randomization</li><li>MERISTOCK™</li><li>SOFTWARE VALIDATION SERVICE</li></ul>
  </div>
</footer>
<div class="footer-base"></div>
</body>
</html>
```